Radiant Crossing - An Exciting Mission & Book Cover Project

Help me to inspire people to live their best life! This is a mission, not just a design project.
I need a Book Cover designed to keep me inspired on the process of writing my book.
Book Title: Radiant Crossing
Tag Line: Three Simple Steps to get out of your own way, SuperCharge your Life and Step into Purpose!
Author: Marlis Quenby

The three steps are: Ownership, Vision and Action (Not sure if this should be on the front or back of the book cover)

The book is a self-help, motivational book. Personal development.
The cover needs to be strong and capture peoples attention, especially with competing shelf space. I almost see a fire ball of flame or explosion that will grab peoples attention.
My company is The Lantern Institute. I have added the company logo and a few pages of my presentation and topic outline to give an idea.
Maybe: The Lantern Institute logo on back of the cover. website is marlisquenby.com

THOUGHT: People should be able to take a photo of them holding the book cover showing what area of life they want Radiant Crossing in. This is why the front cover must be so visual and powerful that they want to take a photo with it. Ie. Explosion, fire, strong and bold.

Target Market(s)

Anyone who feels stuck and needs to breakthrough and move forward in life.

Industry/Entity Type

Motivation

Font styles to use
Serif
Sans Serif

Colors
ec1f27
f37122
fbed22

Requirements
Must have
• The design must be STRONG, SIMPLE, STAND OUT ON BOOK SHELVES.
Must have an open file to swap the photo and copy out.

Back Cover Page
1) Summary
2) 2-3 testimonials. One sentence.
3) About the Author (maybe with photo)
4) Lantern Institute logo
5) Website: radiantcrossing.com and marlisquenby.com
Nice to have
• If my photo works somewhere that would be great. I will change the photo later.
Added Where's Your Harbor? a nice cover example.
Should not have
• Right now I am writing the summary for the back of the cover. For now use Loreum Ipsum text and 2-3 recommendations. Again, I will get these only later.

```html
<!DOCTYPE html>
<html lang="en">
<head>
<meta charset="utf-8">
<title>Radiant Crossing — Book Cover</title>
<link rel="stylesheet" href="https://fonts.googleapis.com/css2?family=Archivo+Black&family=Open+Sans:wght@300;700&display=swap">
<style>
  :root {
    --night: #0c0909;
    --umber: #1d1413;
    --title-tan: #d8b784;
    --tagline-gold: #e9ba58;
    --spark-gold: #f2b636;
    --spark-white: #fff6e0;
    --author-ink: #0b0707;
  }
  * { margin: 0; padding: 0; box-sizing: border-box; }
  html, body { width: 840px; height: 1200px; overflow: hidden; background: var(--night); }
  .cover {
    position: relative;
    width: 840px;
    height: 1200px;
    overflow: hidden;
    background: linear-gradient(to bottom, var(--night) 0, var(--night) 282px, var(--umber) 290px, var(--umber) 100%);
  }
  .burst {
    position: absolute;
    left: 0; top: 500px;
    width: 840px; height: 700px;
    background:
      radial-gradient(ellipse 260px 200px at 680px 620px, var(--spark-white) 0%, rgba(255,240,200,0.85) 35%, rgba(242,182,54,0.6) 60%, rgba(242,182,54,0) 100%),
      radial-gradient(ellipse 520px 420px at 720px 640px, rgba(226,160,60,0.55) 0%, rgba(150,90,40,0.25) 50%, rgba(29,20,19,0) 100%);
  }
  .title {
    position: absolute;
    left: 0; top: 70px;
    width: 840px; height: 290px;
  }
  .title text {
    font-family: "Archivo Black", "Arial Black", sans-serif;
    fill: var(--title-tan);
  }
  .glow-line {
    position: absolute;
    left: 224px; top: 386px;
    width: 424px; height: 8px;
    background: radial-gradient(ellipse at center, #fff3b0 0%, #f5b22a 25%, rgba(245,160,30,0.4) 55%, rgba(245,160,30,0) 100%);
  }
  .tagline {
    position: absolute;
    left: 0; top: 426px;
    width: 840px;
    text-align: center;
    font-family: "Open Sans", sans-serif;
    font-weight: 300;
    font-size: 24px;
    line-height: 35px;
    color: var(--tagline-gold);
    text-transform: uppercase;
  }
  .author {
    position: absolute;
    right: 44px; top: 1108px;
    font-family: "Open Sans", sans-serif;
    font-weight: 700;
    font-size: 52px;
    letter-spacing: 3px;
    color: var(--author-ink);
    text-transform: uppercase;
    white-space: nowrap;
  }
</style>
</head>
<body>
  <main class="cover">
    <div class="burst" role="img" aria-label="Explosion of golden powder and sparks bursting up from the lower right"></div>

    <svg class="title" viewBox="0 0 840 290" aria-label="Radiant Crossing">
      <text x="50" y="150" font-size="165" textLength="742" lengthAdjust="spacingAndGlyphs">RADIANT</text>
      <text x="52" y="272" font-size="86" textLength="740" lengthAdjust="spacingAndGlyphs">CROSSING</text>
    </svg>

    <div class="glow-line"></div>

    <p class="tagline">Three simple steps to get out of your own way,<br>supercharge your life and step into purpose!</p>

    <p class="author">Marlis Quenby</p>
  </main>
</body>
</html>
```